Visitenkarten-Design für Immobilienmakler
Zielgruppe
Immobilienmakler
Aufgabenstellung
Top moderne hochwertige Visitenkate, wir hätten gerne eine sehr hochwertig moderne Visitenkarte mit Bild vom Mitarbeiter... Anbei habe ich die alte Visitenkarte die ich sehr kindlich finde... Es sollte jetzt sehr exklusive aussehen. Alle Daten können von der alten Visitenkarte übernommen werden.. danke

```html
<!DOCTYPE html>
<html lang="de">
<head>
<meta charset="utf-8">
<title>Visitenkarte – Falkner Agentur</title>
<link rel="stylesheet" href="https://fonts.googleapis.com/css2?family=Cinzel:wght@400&family=Roboto+Condensed:wght@300;400;700&display=swap">
<style>
  :root {
    --page-bg: #eceeed;
    --label-grey: #9b9b9b;
    --ink-dark: #2b2a29;
    --paper: #ffffff;
    --brand-green: #1a8a3e;
    --faint-light: #f4f4f4;
    --faint-dark: #353534;
    --faint-dark-inner: #2f2e2d;
  }
  * { margin: 0; padding: 0; box-sizing: border-box; }
  html, body {
    width: 1200px; height: 614px; overflow: hidden;
    background: var(--page-bg);
    font-family: "Roboto Condensed", "Arial Narrow", sans-serif;
  }
  .sheet { position: relative; width: 1200px; height: 614px; }

  .side-label {
    position: absolute; top: 66px; width: 493px; text-align: center;
    font-size: 25px; font-weight: 400; color: var(--label-grey); letter-spacing: 0.5px;
  }
  .side-label--front { left: 88px; }
  .side-label--back { left: 617px; }

  .card {
    position: absolute; top: 153px; width: 493px; height: 322px; overflow: hidden;
  }
  .card--front { left: 88px; background: var(--paper); }
  .card--back { left: 617px; background: var(--ink-dark); }

  .band { position: absolute; left: 0; top: 0; width: 100%; height: 105px; }
  .card--front .band { background: var(--ink-dark); }
  .card--back .band { background: var(--paper); }

  .deco-ring { position: absolute; border-radius: 50%; }
  .card--front .deco-ring--outer { left: -35px; top: 56px; width: 250px; height: 250px; background: var(--faint-light); }
  .card--front .deco-ring--inner { left: 11px; top: 102px; width: 158px; height: 158px; background: var(--paper); }
  .card--back .deco-ring--outer { left: 326px; top: 136px; width: 220px; height: 220px; background: var(--faint-dark); }
  .card--back .deco-ring--inner { left: 366px; top: 176px; width: 140px; height: 140px; background: var(--faint-dark-inner); }

  .wordmark {
    position: absolute; left: 35px; top: 43px;
    display: flex; align-items: center; gap: 8px;
    font-size: 58px; line-height: 58px; font-weight: 700; letter-spacing: -1px;
    white-space: nowrap;
  }
  .card--front .wordmark { color: var(--paper); }
  .card--back .wordmark { color: var(--ink-dark); }
  .wordmark-dot {
    width: 14px; height: 14px; border-radius: 50%; background: var(--brand-green);
    margin-top: 22px;
  }

  .tagline {
    position: absolute; top: 108px; left: 166px;
    font-family: "Cinzel", "Times New Roman", serif;
    font-size: 15px; letter-spacing: 1px; white-space: nowrap;
  }
  .card--front .tagline { color: var(--ink-dark); }
  .card--back .tagline { color: var(--paper); }

  .portrait {
    position: absolute; left: 180px; top: 203px; width: 150px; height: 119px;
    border-radius: 60px 60px 0 0;
    background: linear-gradient(180deg, #cfc2b6 0%, #e9e6e3 55%, #f3f4f6 80%, #3c4a66 100%);
  }

  .holder-name {
    font-family: "Cinzel", "Times New Roman", serif;
    font-size: 23px; line-height: 1; letter-spacing: 0.5px; white-space: nowrap;
  }
  .card--front .holder-name {
    position: absolute; right: 27px; top: 240px; color: var(--ink-dark);
  }
  .front-titles {
    position: absolute; right: 27px; top: 268px; text-align: right;
    color: var(--brand-green); font-size: 15px; line-height: 17px; font-weight: 400;
  }

  .contact-block {
    position: absolute; left: 167px; top: 138px; color: var(--paper);
    font-size: 16px; font-weight: 400; line-height: 1;
  }
  .contact-block .holder-name { color: var(--paper); margin-bottom: 8px; }
  .contact-line { white-space: nowrap; height: 19px; }
  .contact-line--role { font-size: 15px; }
  .contact-line--address { margin-top: 12px; }
  .sep {
    display: inline-block; width: 2px; height: 11px; background: var(--brand-green);
    margin: 0 8px; vertical-align: 0;
  }
  .phone-list { margin-top: 11px; }
  .phone-row { display: flex; height: 19.5px; }
  .phone-key { width: 26px; color: var(--brand-green); font-weight: 700; }
  .web-list { margin-top: 7px; padding-left: 26px; }
  .web-list .contact-line { height: 19.5px; }
</style>
</head>
<body>
<div class="sheet">
  <div class="side-label side-label--front">VORDERSEITE</div>
  <div class="side-label side-label--back">RÜCKSEITE</div>

  <section class="card card--front">
    <div class="deco-ring deco-ring--outer"></div>
    <div class="deco-ring deco-ring--inner"></div>
    <div class="band"></div>
    <div class="wordmark">Falkner Agentur<span class="wordmark-dot"></span></div>
    <div class="tagline">Der Immobilienmakler</div>
    <div class="portrait" role="img" aria-label="Porträtfoto des Mitarbeiters im weißen Hemd mit Sakko über der Schulter"></div>
    <div class="holder-name">Lukas Wendler</div>
    <div class="front-titles">
      <div>Dipl. Immobilienmanager</div>
      <div>Geschäftsführer</div>
    </div>
  </section>

  <section class="card card--back">
    <div class="deco-ring deco-ring--outer"></div>
    <div class="deco-ring deco-ring--inner"></div>
    <div class="band"></div>
    <div class="wordmark">Falkner Agentur<span class="wordmark-dot"></span></div>
    <div class="tagline">Der Immobilienmakler</div>
    <div class="contact-block">
      <div class="holder-name">Lukas Wendler</div>
      <div class="contact-line contact-line--role">Dipl. Immobilienmanager<span class="sep"></span>Geschäftsführer</div>
      <div class="contact-line contact-line--address">Am Lindenweg 12<span class="sep"></span>6850 Feldau</div>
      <div class="phone-list">
        <div class="phone-row"><span class="phone-key">T</span><span>+43 5500 12 345 67</span></div>
        <div class="phone-row"><span class="phone-key">M</span><span>+43 660 0000 123</span></div>
      </div>
      <div class="web-list">
        <div class="contact-line">lukas@falkner-agentur.com</div>
        <div class="contact-line">falkner-agentur.com</div>
      </div>
    </div>
  </section>
</div>
</body>
</html>
```